Thank You For Shopping / Hair Care Tips

I need “Thank You For Shopping”
Post cards made for my hair business !
I added pictures of post cards that I really like . I also added my LuzeKora Wigs logo for you guys to use

I want the backside of the flyer to have hair care tips !
I want people to have full directions on how to care for their wigs

Target Market(s)

Im marking to young woman to older middle aged woman
Ages 23-66 . I want my flyer to look mature And classy

Industry/Entity Type

Hair And Beauty

Font styles to use
Serif
Script

Colors
e34699
e34298
e34398

Requirements
Must have
• The flyer must have the shimmerly logo with my shimmerly name next to it @luze.kora.wigs__
• Also it must have my “Luze Kora Wigs” logo that I’ve uploaded in the pictures section .
• Flyer had to be two sides . One side “ thank you for shopping “ side two “hair care tips”
• My website must be on the flyer - www.luzekorawigs.example
• The flyer must match the colors of my logo
• All white . With the pink and glitter sliver you see on my logo
Nice to have
• Nice to have a glitter border
Should not have
• The flyer should not have different colors that don’t match my logo
• It shouldn’t be made without having my shimmerly or website on the flyer

```html
<!DOCTYPE html>
<html lang="en">
<head>
<meta charset="utf-8">
<title>Luze Kora Wigs – Thank You Postcard</title>
<link rel="stylesheet" href="https://fonts.googleapis.com/css2?family=Mrs+Saint+Delafield&family=Open+Sans:ital,wght@0,300;0,400;0,600;1,400&display=swap">
<style>
  :root {
    --pink: #e34398;
    --silver-light: #e4e4e4;
    --silver-mid: #bdbdbd;
    --silver-dark: #9a9a9a;
    --ink: #444444;
    --paper: #ffffff;
    --backdrop: #fffdd0;
  }
  * { box-sizing: border-box; margin: 0; padding: 0; }
  html, body { width: 1200px; height: 1200px; overflow: hidden; }
  body {
    background: var(--backdrop);
    font-family: "Open Sans", Arial, sans-serif;
    color: var(--ink);
    position: relative;
  }
  .card {
    position: absolute;
    left: 245px;
    width: 661px;
    height: 469px;
    background: var(--paper);
    overflow: hidden;
    box-shadow: 0 8px 10px rgba(0, 0, 0, 0.12);
  }
  .card--front { top: 112px; }
  .card--back { top: 624px; }

  .glitter-frame {
    position: absolute; inset: 0;
    background: linear-gradient(135deg, var(--silver-mid), var(--silver-light) 50%, var(--silver-mid));
  }
  .front-inner {
    position: absolute;
    top: 34px; left: 34px; right: 34px; bottom: 34px;
    background: var(--paper);
    box-shadow: 0 0 16px 10px var(--paper);
  }
  .script {
    font-family: "Mrs Saint Delafield", cursive;
    color: var(--pink);
    font-weight: 400;
    text-align: center;
    position: absolute; left: 0; right: 0;
    white-space: nowrap;
  }
  .front-title { top: 70px; font-size: 64px; line-height: 1; }
  .brand-name {
    position: absolute; left: 0; right: 0; top: 200px;
    text-align: center;
    font-family: "Open Sans", Arial, sans-serif;
    font-weight: 400;
    font-size: 52px;
    color: var(--pink);
    letter-spacing: 1px;
  }
  .contact-row {
    position: absolute; top: 378px; left: 0; right: 0;
    display: flex; justify-content: center; gap: 44px;
    font-style: italic; font-size: 20px; color: var(--ink);
  }
  .contact-item { display: flex; align-items: center; gap: 6px; }
  .contact-item svg { flex: none; }

  .back-title { top: 26px; font-size: 80px; line-height: 1; }
  .tips {
    position: absolute; left: 52px; right: 16px; top: 134px;
    font-size: 9.6px; font-weight: 300; line-height: 13.5px;
    list-style: none;
  }
  .tips li { position: relative; padding-left: 14px; }
  .tips li::before {
    content: "✔"; position: absolute; left: 0; top: 0;
    color: var(--pink); font-size: 9px;
  }
  .tips-heading {
    position: absolute; left: 66px; top: 270px;
    font-size: 9.6px; font-weight: 600; color: var(--ink);
  }
  .tips--night { top: 284px; }
  .social-band {
    position: absolute; left: 0; right: 0; top: 362px; height: 47px;
    background: var(--pink); color: var(--paper);
    display: flex; align-items: center; justify-content: center; gap: 18px;
    font-size: 20px;
  }
  .social-band .handle { font-style: italic; font-size: 26px; display: flex; align-items: center; gap: 10px; }
  .glitter-strip {
    position: absolute; left: 0; right: 0; bottom: 0; height: 50px;
    background: linear-gradient(to bottom, var(--paper), var(--silver-light) 35%, var(--silver-dark));
  }
</style>
</head>
<body>

<section class="card card--front">
  <div class="glitter-frame" role="img" aria-label="Silver glitter border around the card"></div>
  <div class="front-inner"></div>
  <h1 class="script front-title">Thank You For Shopping</h1>
  <p class="brand-name">Luze Kora Wigs</p>
  <div class="contact-row">
    <span class="contact-item">
      <svg width="20" height="20" viewBox="0 0 20 20" aria-hidden="true"><circle cx="10" cy="10" r="8.5" fill="none" stroke="var(--pink)" stroke-width="1.6"/></svg>
      @luze.kora.wigs__
    </span>
    <span class="contact-item">
      <svg width="20" height="20" viewBox="0 0 20 20" aria-hidden="true"><circle cx="10" cy="10" r="8.5" fill="none" stroke="var(--pink)" stroke-width="1.6"/></svg>
      www.luzekorawigs.example
    </span>
  </div>
</section>

<section class="card card--back">
  <h2 class="script back-title">Hair Care Tips</h2>
  <ul class="tips">
    <li>Apply a moisture rich Conditioner and comb hair, starting with the ends working your way up to your scalp.</li>
    <li>Leave Conditioner in for at least 15 minutres or more</li>
    <li>Do not massage the hair</li>
    <li>Rinse thoroughly</li>
    <li>Scrunch hair gently to ehnance the curs. (For wavy/curly patterns)</li>
    <li>When damp, apply a dime size of an anti-frizz alcohol free hair serum.</li>
    <li>Let air-dry</li>
    <li>Do not use oil products or excessive products on curly hair, it will cause matting.</li>
    <li>Do not brush or comb hair when dry, it will cause hair to frizz and may cause hair to tangle.</li>
  </ul>
  <h3 class="tips-heading">BED TIME CARE</h3>
  <ul class="tips tips--night">
    <li>Before going to bed, braid your hair into one loose large braid and wear a sating scarf or bonnet.</li>
    <li>After waking up, undo braid and comb using a wide tooth comb (or paddle brush) through begining at the ends and working your way up to roots.</li>
    <li>Style as needed.</li>
  </ul>
  <div class="social-band">
    <span>Tags us on shimmerly</span>
    <span class="handle">
      <svg width="22" height="22" viewBox="0 0 22 22" aria-hidden="true"><circle cx="11" cy="11" r="9.5" fill="none" stroke="var(--paper)" stroke-width="1.6"/></svg>
      @luze.kora.wigs__
    </span>
  </div>
  <div class="glitter-strip" role="img" aria-label="Silver glitter confetti along the bottom edge"></div>
</section>

</body>
</html>
```